"Heartland Pour Days" Americana themed festival flyer

We are looking for a flier to promote our Americana themed festival at Marlowe Creek Brewing Company here in New Orleans, LA. It is a family Friendly 2 day event over Labor Day weekend. The Name of the event is "Heartland Pour Days". Our goal is is to have a designer follow a letterpress style of typography and design while following a standard festival flier composition. if possible we would also like to include illustrations of the brewery tower and the tank in front of our building. (images provided)

Target Market(s)

People interested in Bluegrass music and Americana grass roots style events.

Industry/Entity Type

Beer

Font styles to use
Serif

Colors
0054AA
0677BA
7BADD7
CADEEF
E8F1F8
EB3D1F
EC4F4E
F09395
F8D3D4
FCEDEE

Requirements
Must have
• Letterpress Style typography and Illustrations of the Brewery tower and tank at the front of the brewery.

```html
<!DOCTYPE html>
<html lang="en">
<head>
<meta charset="utf-8">
<title>Heartland Pour Days – Americana Festival</title>
<link rel="stylesheet" href="https://fonts.googleapis.com/css2?family=Bebas+Neue&family=Oswald:wght@500;600&family=Rye&display=swap">
<style>
:root{
  --frame-black:#000;
  --border-red:#df4647;
  --paper-pink:#f1d0d2;
  --title-blue:#1a6db3;
  --pill-blue:#0677BA;
  --accent-red:#ec4f4e;
  --name-navy:#2a3d6e;
  --icon-pink:#f09395;
}
*{margin:0;padding:0;box-sizing:border-box}
html,body{width:955px;height:1200px;overflow:hidden;background:var(--frame-black)}
.canvas{position:relative;width:955px;height:1200px;background:var(--frame-black)}
.poster{position:absolute;left:98px;top:109px;width:759px;height:981px;background:var(--border-red);overflow:hidden}
.paper{position:absolute;left:22px;top:26px;width:715px;height:925px;background:var(--paper-pink);border-radius:18px 24px 14px 20px;box-shadow:0 0 14px 6px var(--paper-pink) inset}
.brewery-scene{position:absolute;left:120px;top:845px;width:700px;height:210px;
  background:linear-gradient(180deg,rgba(241,208,210,0) 0%,rgba(226,150,152,.55) 45%,rgba(205,110,112,.8) 100%)}
.abs{position:absolute;text-align:center;white-space:nowrap}
.event-name{left:98px;width:759px;top:163px;font-family:"Bebas Neue",sans-serif;font-size:62px;color:var(--title-blue);letter-spacing:1px}
.rule-star{position:absolute;left:252px;top:232px;width:364px;height:12px}
.title-arc{position:absolute;left:150px;top:250px;width:650px;height:180px}
.dates{left:98px;width:759px;top:358px;font-family:"Bebas Neue",sans-serif;font-size:34px;color:var(--title-blue)}
.dates sup{font-size:15px;vertical-align:14px}
.hours{left:98px;width:759px;top:404px;font-family:"Bebas Neue",sans-serif;font-size:34px;color:var(--accent-red)}
.hours-rule{position:absolute;left:402px;width:151px;height:2px;background:var(--accent-red)}
.pill{position:absolute;height:42px;background:var(--pill-blue);color:#fff;font-family:"Oswald",sans-serif;font-weight:500;font-size:24px;line-height:40px;text-align:center;border-radius:6px 14px 10px 4px;transform:skewX(-4deg)}
.slot{position:absolute;left:240px;width:200px;text-align:center}
.slot .time{font-family:"Bebas Neue",sans-serif;font-size:24px;line-height:24px;color:var(--accent-red)}
.slot .act{font-family:"Bebas Neue",sans-serif;font-size:16px;line-height:16px;color:var(--name-navy);letter-spacing:.3px}
.list{position:absolute;left:500px;width:300px;text-align:center;font-family:"Bebas Neue",sans-serif;font-size:16.5px;line-height:20.5px;color:var(--accent-red);letter-spacing:.3px}
.list .blue{color:var(--title-blue)}
.icon{position:absolute;background:var(--icon-pink);opacity:.55;border-radius:10px}
.brewery-name{position:absolute;left:590px;top:928px;font-family:"Bebas Neue",sans-serif;font-size:26px;color:#b36b6d;opacity:.8}
</style>
</head>
<body>
<div class="canvas">
  <div class="poster">
    <div class="paper"></div>
  </div>
  <div class="brewery-scene" role="img" aria-label="Illustration of the brewery building with its tower and tank in front"></div>
  <div class="brewery-name">Marlowe Creek Brewing Co</div>

  <div class="abs event-name">HEARTLAND POUR DAYS</div>
  <svg class="rule-star" viewBox="0 0 364 12">
    <line x1="0" y1="6" x2="364" y2="6" stroke="#ec4f4e" stroke-width="1.5"/>
    <circle cx="182" cy="6" r="5" fill="#ec4f4e"/>
  </svg>
  <svg class="title-arc" viewBox="0 0 650 180">
    <path id="arcPath" d="M18 150 Q325 10 632 150" fill="none"/>
    <path d="M20 160 Q325 30 630 160" fill="none" stroke="#ec4f4e" stroke-width="2.5"/>
    <text font-family="Rye, serif" font-size="62" fill="#ec4f4e" transform="translate(2,3)">
      <textPath href="#arcPath" textLength="610" lengthAdjust="spacingAndGlyphs">AMERICANA FESTIVAL</textPath>
    </text>
    <text font-family="Rye, serif" font-size="62" fill="#1a6db3">
      <textPath href="#arcPath" textLength="610" lengthAdjust="spacingAndGlyphs">AMERICANA FESTIVAL</textPath>
    </text>
  </svg>

  <div class="abs dates">SATURDAY, SEPT 5<sup>TH</sup> &amp; 6<sup>TH</sup></div>
  <div class="hours-rule" style="top:399px"></div>
  <div class="abs hours">11AM-8PM</div>
  <div class="hours-rule" style="top:444px"></div>

  <!-- Entertainment -->
  <div class="pill" style="left:259px;top:459px;width:164px">Entertainment</div>
  <div class="icon" style="left:172px;top:562px;width:92px;height:83px" role="img" aria-label="Drummer icon"></div>
  <div class="slot" style="top:511px"><div class="time">11:30AM-1PM</div><div class="act">Porchlight Jam Session</div></div>
  <div class="slot" style="top:562px"><div class="time">1:30PM-3PM</div><div class="act">Rusty Spurs</div></div>
  <div class="slot" style="top:615px"><div class="time">3:30PM-5PM</div><div class="act">Wyatt Calloway</div></div>
  <div class="slot" style="top:667px"><div class="time">5:30PM-7PM</div><div class="act">Dolly Hart &amp; The Dancehall<br>Revue</div></div>
  <div class="slot" style="top:743px"><div class="time">11:30AM-1PM</div><div class="act">Porchlight Jam Session</div></div>
  <div class="slot" style="top:792px"><div class="time">1:30PM-3PM</div><div class="act">June Mercer Bluegrass Debut</div></div>
  <div class="slot" style="top:846px"><div class="time">3:30PM-5PM</div><div class="act">Cypress Bayou<br>Country Breakdown</div></div>
  <div class="slot" style="top:916px"><div class="time">5:30PM-7PM</div><div class="act">Prairie Line</div></div>

  <!-- Activities -->
  <div class="pill" style="left:567px;top:459px;width:167px">Activities</div>
  <div class="icon" style="left:456px;top:520px;width:75px;height:78px" role="img" aria-label="Arts and music icon"></div>
  <div class="list" style="top:507px">ART MARKET <span class="blue">(30 VENDORS &nbsp;12PM-6PM)</span><br>YARD GAMES<br>FACE PAINTING</div>

  <div class="pill" style="left:567px;top:578px;width:167px">Food Vendors</div>
  <div class="icon" style="left:462px;top:631px;width:72px;height:75px" role="img" aria-label="Food stall icon"></div>
  <div class="list" style="top:626px">BON TEMPS BITES<br>BBQ<br>BIG CHILL POPSICLES<br>GOURMET POPCORN<br>SUGAR SWIRL</div>

  <div class="pill" style="left:567px;top:733px;width:167px">Beneficiary</div>
  <div class="icon" style="left:442px;top:729px;width:111px;height:58px" role="img" aria-label="Person playing with a dog icon"></div>
  <div class="list" style="top:782px;left:470px;width:360px">CRESCENT PAWS RESCUE PRESENCE/TENT<br>DOGGIE PHOTOBOOTH<br>% OF PUP PANTRY TOYS DONATED BACK TO RESCUE</div>
</div>
</body>
</html>
```